Refrigeration & Air Conditioning modern and appealing

We want to design a business card that is modern and appealing using existing logo supplied

Front card
Residential Commercial Diary
RTA : AU071523
Licence L258907

Back card
Marcus Ovenly
Director
0491 352 406
info@frostvalecooling.com.au
www.frostvalecooling.com.au
• Air Conditioning
• Cool Rooms & Refrigeration
• Installation
• Service & Repair
• Preventative Maintenance

We offer 24/7 emergency service

```html
<!DOCTYPE html>
<html lang="en">
<head>
<meta charset="utf-8">
<title>Frostvale Cooling – Business Card</title>
<link rel="stylesheet" href="https://fonts.googleapis.com/css2?family=Lato:wght@400;700&family=Montserrat:wght@400;500;700&family=Orbitron:wght@700;800&display=swap">
<style>
  :root {
    --backdrop: #939393;
    --card-dark: #1c1b1d;
    --card-dark-edge: #0f0f10;
    --card-light: #ffffff;
    --purple: #8c5bb0;
    --purple-soft: #a987c8;
    --lilac: #c9c3e6;
    --ink: #111111;
    --white: #ffffff;
    --divider: #b89ad0;
  }
  * { box-sizing: border-box; margin: 0; padding: 0; }
  html, body { width: 1200px; height: 1000px; overflow: hidden; }
  body { background: var(--backdrop); position: relative; font-family: "Lato", sans-serif; }

  .card { position: absolute; left: 212px; width: 776px; border-radius: 18px; overflow: hidden; }
  .card-front { top: 46px; height: 444px;
    background: radial-gradient(ellipse at 60% 40%, #262527 0%, var(--card-dark) 55%, var(--card-dark-edge) 100%); }
  .card-back { top: 510px; height: 443px; background: var(--card-light); }

  .brand-motif { position: absolute; left: 0; top: 0; width: 280px; height: 100%;
    background: radial-gradient(ellipse 100% 60% at 0% 52%, var(--purple) 0%, rgba(169,135,200,0.75) 35%, rgba(201,195,230,0.25) 62%, rgba(28,27,29,0) 78%); }

  .brand { position: absolute; display: flex; align-items: center; gap: 12px;
    font-family: "Montserrat", sans-serif; font-weight: 700; letter-spacing: 1px; white-space: nowrap; }
  .brand-mark { border-radius: 50%; background: var(--purple); flex: none; }
  .brand-front { right: 38px; top: 40px; font-size: 34px; color: var(--white); }
  .brand-front .brand-mark { width: 48px; height: 48px; }
  .brand-back { right: 38px; top: 24px; width: 236px; flex-direction: column; gap: 14px;
    font-size: 34px; color: var(--ink); }
  .brand-back .brand-mark { width: 64px; height: 64px; }

  .credentials { position: absolute; right: 36px; top: 324px; text-align: right;
    font-family: "Montserrat", sans-serif; font-size: 20px; line-height: 28px; color: var(--white); }
  .credentials .label { color: var(--purple-soft); }
  .sectors { position: absolute; right: 38px; top: 396px; font-size: 20px; color: var(--white); }

  .person-name { position: absolute; left: 43px; top: 36px; font-family: "Orbitron", sans-serif;
    font-weight: 800; font-size: 29px; letter-spacing: 1.5px; color: var(--purple); text-transform: uppercase; }
  .person-role { position: absolute; left: 43px; top: 74px; font-size: 18px; color: var(--ink); }

  .contact-list { position: absolute; left: 43px; top: 122px; list-style: none;
    font-family: "Montserrat", sans-serif; font-size: 18px; color: var(--ink); }
  .contact-list li { display: flex; align-items: center; gap: 12px; height: 34px; }
  .contact-icon { width: 24px; height: 24px; border: 1.6px solid var(--purple); border-radius: 5px;
    display: flex; align-items: center; justify-content: center; }

  .services { position: absolute; left: 22px; right: 22px; top: 244px; height: 116px; display: flex; }
  .service { flex: 1; display: flex; flex-direction: column; align-items: center; text-align: center;
    font-size: 17px; line-height: 22px; color: var(--ink); border-left: 1.5px dashed var(--divider); }
  .service:first-child { border-left: none; }
  .service svg { height: 52px; width: 60px; margin: 4px 0 10px; }

  .emergency { position: absolute; left: 0; right: 0; top: 386px; text-align: center;
    font-family: "Montserrat", sans-serif; font-weight: 700; font-size: 21px; color: var(--ink); }
  .emergency .accent { color: var(--purple); }
  .emergency .rule { display: inline-block; width: 28px; height: 2px; background: var(--purple);
    vertical-align: middle; margin: 0 8px; }
</style>
</head>
<body>

<section class="card card-front">
  <div class="brand-motif" role="img" aria-label="Large brand snowflake motif"></div>
  <div class="brand brand-front"><span class="brand-mark"></span>FROSTVALE</div>
  <div class="credentials">
    <p><span class="label">RTA :</span> AU071523</p>
    <p><span class="label">Licence</span> L258907</p>
  </div>
  <p class="sectors">Residential Commercial Diary</p>
</section>

<section class="card card-back">
  <h1 class="person-name">Marcus Ovenly</h1>
  <p class="person-role">Director</p>

  <div class="brand brand-back"><span class="brand-mark"></span>FROSTVALE</div>

  <ul class="contact-list">
    <li><span class="contact-icon"><svg width="14" height="14" viewBox="0 0 24 24" fill="none" stroke="#8c5bb0" stroke-width="2.4"><path d="M5 3h4l2 5-3 2a11 11 0 0 0 6 6l2-3 5 2v4a2 2 0 0 1-2 2A18 18 0 0 1 3 5a2 2 0 0 1 2-2z"/></svg></span>0491 352 406</li>
    <li><span class="contact-icon"><svg width="14" height="14" viewBox="0 0 24 24" fill="none" stroke="#8c5bb0" stroke-width="2.4"><path d="M22 2 2 10l8 3 3 8z"/><path d="M22 2 10 13"/></svg></span>info@frostvalecooling.com.au</li>
    <li><span class="contact-icon"><svg width="14" height="14" viewBox="0 0 24 24" fill="none" stroke="#8c5bb0" stroke-width="2.2"><circle cx="12" cy="12" r="9"/><path d="M3 12h18M12 3c3 3 3 15 0 18M12 3c-3 3-3 15 0 18"/></svg></span>www.frostvalecooling.com.au</li>
  </ul>

  <div class="services">
    <div class="service">
      <svg viewBox="0 0 60 52" fill="none" stroke="#8c5bb0" stroke-width="2"><rect x="4" y="8" width="52" height="20" rx="3"/><path d="M10 22h40M22 34v6M30 34v8M38 34v6"/></svg>
      Air Conditioning
    </div>
    <div class="service">
      <svg viewBox="0 0 60 52" fill="none" stroke="#8c5bb0" stroke-width="2"><path d="M8 22 30 4l22 18M13 18v30h34V18"/><circle cx="30" cy="32" r="10"/><path d="M30 32v-8M30 32l7 4M30 32l-7 4"/></svg>
      Cool Rooms &amp;<br>Refrigeration
    </div>
    <div class="service">
      <svg viewBox="0 0 60 52" fill="none" stroke="#8c5bb0" stroke-width="2"><circle cx="30" cy="26" r="15" stroke-dasharray="6 3" stroke-width="5"/><circle cx="30" cy="26" r="9"/><path d="m25 26 4 4 6-7"/></svg>
      Installation
    </div>
    <div class="service">
      <svg viewBox="0 0 60 52" fill="none" stroke="#8c5bb0" stroke-width="2"><path d="M14 6 46 42M10 10l8-2-2 8zM46 8a7 7 0 0 0-8 9L16 40a4 4 0 1 0 5 5l22-22a7 7 0 0 0 9-8l-5 4-4-1-1-4z"/></svg>
      Service &amp; Repair
    </div>
    <div class="service">
      <svg viewBox="0 0 60 52" fill="none" stroke="#8c5bb0" stroke-width="2"><path d="M30 4c-6 9-12 15-12 23a12 12 0 0 0 24 0c0-8-6-14-12-23z"/><circle cx="30" cy="27" r="5"/><path d="M6 42h10l10 4h14l10-6"/><circle cx="19" cy="8" r="4"/></svg>
      Preventative<br>Maintenance
    </div>
  </div>

  <p class="emergency"><span class="rule"></span>WE OFFER <span class="accent">24/7 EMERGENCY SERVICE</span><span class="rule"></span></p>
</section>

</body>
</html>
```